Norvane Labs - Methylene Blue Product Packaging

Our brand is Norvane Labs. We are launching a new product that is Methylene Blue, you can see more about this product if you search on Quorvix or Brellto and you will see what it is. This will be for a 50ml bottle. Give me different options for packaging that is minimalist and clean for this brand that makes it look well made and make people want to buy. I've added examples of what the bottle shape will be and potential packaging shapes so you can make packaging on those based off of that.

```html
<!DOCTYPE html>
<html lang="en">
<head>
<meta charset="utf-8">
<title>Norvane Labs – Methylene Blue Label</title>
<link rel="stylesheet" href="https://fonts.googleapis.com/css2?family=Montserrat:wght@600;700&family=Nunito:wght@700&display=swap">
<style>
  :root {
    --backdrop: #e6e6e6;
    --label-white: #ffffff;
    --pattern-warm: #f6efdf;
    --ink: #111111;
    --navy: #1a1aa6;
    --royal: #0a3fc0;
    --sky: #0aa4e0;
    --gold: #c89b2a;
    --gold-light: #f1dfa6;
    --text-blue: #1c1a8f;
    --stroke-deep: #1a55e6;
    --stroke-light: #9fd6f5;
  }
  * { box-sizing: border-box; margin: 0; padding: 0; }
  html, body { width: 1082px; height: 1200px; overflow: hidden; }
  body {
    background: var(--backdrop);
    display: flex;
    align-items: center;
    justify-content: center;
  }
  .label {
    position: relative;
    width: 600px;
    height: 1040px;
    background: var(--label-white);
    overflow: hidden;
  }
  .label__pattern {
    position: absolute;
    inset: 0;
    background:
      radial-gradient(circle at 50% 15%, var(--pattern-warm) 0%, transparent 45%),
      radial-gradient(circle at 8% 60%, var(--pattern-warm) 0%, transparent 30%),
      radial-gradient(circle at 95% 55%, var(--pattern-warm) 0%, transparent 30%),
      radial-gradient(circle at 55% 97%, var(--pattern-warm) 0%, transparent 30%),
      var(--label-white);
  }
  .brand {
    position: absolute;
    top: 232px;
    left: 80px;
    width: 440px;
    font-family: "Montserrat", sans-serif;
    font-weight: 700;
    color: var(--ink);
    text-align: right;
  }
  .brand__name {
    display: block;
    font-size: 80px;
    line-height: 84px;
    letter-spacing: -2px;
    text-align: center;
  }
  .brand__suffix {
    display: block;
    font-size: 50px;
    line-height: 54px;
    letter-spacing: -1px;
    margin-right: 10px;
  }
  .product-box {
    position: absolute;
    top: 410px;
    left: 74px;
    width: 452px;
    height: 272px;
    border-radius: 16px;
    border: 3px solid var(--royal);
    border-right-color: var(--sky);
    background: var(--label-white);
    overflow: hidden;
  }
  .product-box__title {
    height: 142px;
    background: linear-gradient(90deg, var(--navy) 0%, var(--royal) 50%, var(--sky) 100%);
    color: #fff;
    font-family: "Montserrat", sans-serif;
    font-weight: 600;
    font-size: 50px;
    line-height: 58px;
    letter-spacing: 1px;
    text-align: center;
    padding-top: 14px;
  }
  .product-box__rule {
    width: 60px;
    height: 3px;
    background: var(--gold);
    margin: 24px auto 20px;
  }
  .product-box__spec {
    font-family: "Nunito", sans-serif;
    font-weight: 700;
    font-size: 24px;
    line-height: 33px;
    color: var(--text-blue);
    text-align: center;
  }
  .stroke-placeholder {
    position: absolute;
    top: 712px;
    left: 64px;
    width: 472px;
    height: 200px;
    background: linear-gradient(90deg, var(--stroke-deep) 0%, var(--stroke-light) 100%);
  }
  .volume-band {
    position: absolute;
    top: 958px;
    left: 0;
    right: 0;
    height: 10px;
    background: linear-gradient(90deg, var(--gold) 0%, var(--gold-light) 50%, var(--gold) 100%);
  }
  .volume-tag {
    position: absolute;
    top: 922px;
    left: 246px;
    width: 108px;
    height: 42px;
    background: linear-gradient(90deg, var(--gold) 0%, var(--gold-light) 100%);
    clip-path: polygon(8% 0, 100% 0, 92% 100%, 0 100%);
    font-family: "Nunito", sans-serif;
    font-weight: 700;
    font-size: 26px;
    line-height: 42px;
    text-align: center;
    color: var(--ink);
  }
</style>
</head>
<body>
  <main class="label">
    <div class="label__pattern" role="img" aria-label="Gold molecular structure pattern across the white label"></div>

    <div class="brand">
      <span class="brand__name">Norvane</span>
      <span class="brand__suffix">Labs</span>
    </div>

    <section class="product-box">
      <h1 class="product-box__title">METHYLENE<br>BLUE</h1>
      <div class="product-box__rule"></div>
      <p class="product-box__spec">10% Methylene Blue Solution<br>USP (Pharma) Grade</p>
    </section>

    <div class="stroke-placeholder" role="img" aria-label="Blue paint brush stroke illustration"></div>

    <div class="volume-band"></div>
    <div class="volume-tag">50ml</div>
  </main>
</body>
</html>
```